Project Planning & Communication Process

Need a PowerPoint slide that illustrates our project planning and communication cycle. Our company has key meetings, and key communication vehicles (like emails and follow up tools) that we use to ensure our frontline staff are prepared to execute the new project successfully. This document needs to call out how the different components, like the meetings and emails, work together (like a flow chart), so someone who needs to use this process will understand what they should do. The slide needs to be simple yet comprehensive enough to guide someone through the details. I don't want it overwhelming. The primary focus is the process, not the details.

Use the color pallette included within the slide (shades of blue and gray, and black). This is for an insurance company (www.harborquill.com). Use this as a reference for the look and feel.

I have attached a sample slide of the flow chart process.

Click here if you cannot access the file. https://www.filecrate.example/s/q8wz2mbt7ypnc4r/Communcation_Methods_V1.pptx

If you are not able to see the uploaded slide.  Please send me your email address and I will send the slide to you directly. 

ISince I'm not able to upload the reference ppt file, 've uploaded the slide at FileCrate.  Please click here to access.
https://www.filecrate.example/s/q8wz2mbt7ypnc4r/Communcation_Methods_V1.pptx

Reason: extending one more day for designers to make last minute updates.

Target Market(s)

Vice Presidents and project managers/business partners within the organization.

Industry/Entity Type

Communication

Font styles to use
Sans Serif

Colors
3176b5

Requirements
Must have
• 1 page, color pallette assigned, be simple yet comprehensive. the focus needs to be on the process, not on the details.
Nice to have
• Doesn't have to follow the example I provided. Please feel free to approach from different ways.

```html
<!DOCTYPE html>
<html lang="en">
<head>
<meta charset="utf-8">
<title>Project Alignment &amp; Project Communication Process</title>
<link href="https://fonts.googleapis.com/css2?family=Carlito:wght@400;700&display=swap" rel="stylesheet">
<style>
  :root {
    --white: #ffffff;
    --title-grey: #a5a5a5;
    --pale-grey: #f2f2f2;
    --light-grey: #d9d9d9;
    --mid-grey: #bfbfbf;
    --dark-grey: #7f7f7f;
    --meeting-blue: #4f81bd;
    --meeting-blue-dark: #3c6aa3;
    --navy: #13254a;
    --arrow: #b4c3dc;
    --ink: #1a1a1a;
  }
  * { box-sizing: border-box; margin: 0; padding: 0; }
  html, body { width: 1200px; height: 900px; overflow: hidden; background: var(--white); }
  body { font-family: "Carlito", "Calibri", Arial, sans-serif; color: var(--ink); }
  .slide { position: relative; width: 1200px; height: 900px; overflow: hidden; }
  .block { position: absolute; display: flex; flex-direction: column; justify-content: center; }

  .title-bar {
    left: 0; top: 10px; width: 1200px; height: 60px;
    background: linear-gradient(var(--title-grey), #959595);
    color: var(--white); font-weight: 700; font-size: 31px;
    align-items: center; padding-right: 60px;
  }
  .phase-label { background: var(--pale-grey); font-weight: 700; font-size: 20px; align-items: center; }
  .phase-label.prepare { background: var(--mid-grey); }
  .phase-label.evaluate { background: var(--dark-grey); color: var(--white); font-weight: 400; font-size: 21px; }

  .timeline-bar { background: var(--light-grey); font-weight: 700; font-size: 16px; align-items: center; }
  .timeline-bar.top { background: var(--pale-grey); }

  .step { align-items: center; text-align: center; color: var(--white); font-size: 15px; line-height: 1.1; padding: 4px 8px; }
  .step.pending { background: var(--light-grey); }
  .step.meeting { background: var(--meeting-blue); font-weight: 700; border: 1px solid var(--meeting-blue-dark); }
  .step.meeting.tall { justify-content: flex-start; padding-top: 10px; border-radius: 6px; align-items: flex-start; text-align: left; padding-left: 10px; }
  .step.meeting.tall .step-title { font-size: 15px; }
  .step .step-note { font-size: 10.5px; margin-top: 8px; font-weight: 700; }
  .step .step-note + .step-note { margin-top: 10px; }

  .prep-meeting { background: var(--meeting-blue); border: 1px solid var(--meeting-blue-dark); border-radius: 6px;
    color: var(--white); font-weight: 700; text-align: center; padding: 8px 6px; justify-content: flex-start; }
  .prep-meeting .step-title { font-size: 15px; line-height: 1.15; }
  .prep-meeting .step-note { font-size: 12px; margin-top: 12px; line-height: 1.2; }
  .prep-meeting .step-note.when { margin-top: 14px; }

  .tool { background: var(--navy); border-radius: 9px; color: var(--white); align-items: center; text-align: center; font-size: 14.5px; line-height: 1.2; }
  .tool .tool-name.bold { font-weight: 700; }
  .tool .tool-sub { font-size: 11.5px; margin-top: 14px; }
  .tool .tool-line + .tool-line { margin-top: 36px; }

  .note { background: var(--pale-grey); font-size: 13.5px; line-height: 1.22; padding: 6px 8px; justify-content: flex-start; }
  .note.center { justify-content: center; }
  .note.grey { background: var(--light-grey); }
  .note b { font-weight: 700; }

  .arrow { position: absolute; width: 18px; height: 18px; }
  .arrow path { fill: var(--arrow); }

  .legend { color: var(--white); align-items: center; }
  .legend.meetings { background: var(--meeting-blue); font-size: 24px; }
  .legend.tools { background: var(--navy); font-size: 22px; border-radius: 5px; }
</style>
</head>
<body>
<div class="slide">

  <div class="block title-bar">Project Alignment &amp; Project Communication Process</div>

  <!-- Planning & Design Phase -->
  <div class="block phase-label" style="left:0;top:76px;width:320px;height:39px;">Planning &amp; Design Phase</div>
  <div class="block timeline-bar top" style="left:0;top:125px;width:790px;height:36px;">3 + Months out</div>
  <div class="block timeline-bar top" style="left:812px;top:125px;width:385px;height:36px;">2 + Months out</div>

  <div class="block step pending" style="left:2px;top:179px;width:175px;height:40px;">New Project Identified</div>
  <div class="block step meeting" style="left:210px;top:179px;width:165px;height:40px;font-weight:400;">Governance Meeting</div>
  <div class="block step pending" style="left:410px;top:179px;width:191px;height:40px;">Separate Project<br>Meetings as needed</div>
  <div class="block step meeting" style="left:634px;top:179px;width:155px;height:40px;font-weight:400;">Governance<br>Meeting</div>
  <div class="block step meeting" style="left:814px;top:179px;width:194px;height:44px;">Weekly Center Leader<br>Meeting</div>
  <div class="block step meeting tall" style="left:1037px;top:171px;width:157px;height:106px;">
    <span class="step-title">Field Advisory Panel</span>
    <span class="step-note">Purpose: Collect Feedback</span>
    <span class="step-note">When: As needed</span>
  </div>

  <svg class="arrow" style="left:181px;top:190px;" viewBox="0 0 18 18"><path d="M0 5h9V0l9 9-9 9v-5H0z"/></svg>
  <svg class="arrow" style="left:381px;top:190px;" viewBox="0 0 18 18"><path d="M0 5h9V0l9 9-9 9v-5H0z"/></svg>
  <svg class="arrow" style="left:608px;top:190px;" viewBox="0 0 18 18"><path d="M0 5h9V0l9 9-9 9v-5H0z"/></svg>
  <svg class="arrow" style="left:794px;top:190px;" viewBox="0 0 18 18"><path d="M0 5h9V0l9 9-9 9v-5H0z"/></svg>
  <svg class="arrow" style="left:1015px;top:190px;" viewBox="0 0 18 18"><path d="M0 5h9V0l9 9-9 9v-5H0z"/></svg>

  <div class="block note center" style="left:216px;top:231px;width:160px;height:48px;"><p><b>Purpose:</b> Go/No Go Decision</p></div>
  <div class="block note" style="left:216px;top:290px;width:164px;height:138px;"><p><b>Overview:</b> Project Owner presents one pager to Sr Leadership. Based on Business Value, and Capacity a Go/No Go Decision is made.</p></div>

  <div class="block note" style="left:639px;top:230px;width:151px;height:84px;"><p><b>Purpose:</b> Report out on Milestone status and Key Decision Points</p></div>
  <div class="block note" style="left:639px;top:330px;width:151px;height:138px;"><p><b>Overview:</b> Project Owner presents one pager to Sr Leadership. Based on Business Value, and Capacity a Go/No Go Decision is made.</p></div>

  <div class="block note" style="left:815px;top:234px;width:193px;height:66px;"><p><b>Purpose:</b> Introduce Project &amp; gather Center Leader Feedback</p></div>
  <div class="block note" style="left:815px;top:315px;width:193px;height:84px;"><p><b>Overview:</b> Project Owner provides overview of project, collects center leader feedback.</p></div>

  <div class="block note center" style="left:1037px;top:291px;width:157px;height:48px;"><p><b>Purpose:</b> Collect Center Staff Feedback</p></div>
  <div class="block note" style="left:1037px;top:356px;width:157px;height:83px;"><p><b>Overview:</b> Project Owner presents project and collect Center Staff Feedback</p></div>

  <!-- Prepare Phase -->
  <div class="block phase-label prepare" style="left:0;top:460px;width:320px;height:39px;">Prepare Phase</div>
  <div class="block phase-label evaluate" style="left:330px;top:460px;width:278px;height:39px;">Follow Up &amp; Evaluate</div>

  <div class="block timeline-bar" style="left:0;top:516px;width:186px;height:34px;">1 month out</div>
  <div class="block timeline-bar" style="left:218px;top:516px;width:655px;height:34px;">1 Week out</div>

  <div class="block prep-meeting" style="left:0;top:564px;width:186px;height:137px;">
    <span class="step-title">Weekly Center Leader Meeting</span>
    <span class="step-note">Purpose: Center Planning and Specific execution details</span>
    <span class="step-note when">When: 1 month out</span>
  </div>
  <div class="block note grey" style="left:0;top:714px;width:186px;height:65px;"><p><b>Purpose:</b> Provide Center Leaders with Implementation Details</p></div>
  <div class="block note grey" style="left:0;top:792px;width:186px;height:104px;"><p><b>Overview:</b> Project Owner presents project and implementation details to ensure Center Leaders are prepared.</p></div>

  <div class="block tool" style="left:215px;top:566px;width:196px;height:137px;">
    <span class="tool-line">Monday Memo</span>
    <span class="tool-line">1 week out</span>
  </div>
  <div class="block tool" style="left:440px;top:570px;width:196px;height:133px;">
    <span class="tool-name bold">Daily Digest</span>
    <span class="tool-sub">Just in Time Notice/Follow up for execution</span>
  </div>
  <div class="block tool" style="left:675px;top:570px;width:196px;height:133px;">
    <span class="tool-line">Follow Up Guide</span>
    <span class="tool-line">Post Launch</span>
  </div>

  <svg class="arrow" style="left:193px;top:623px;" viewBox="0 0 18 18"><path d="M0 5h9V0l9 9-9 9v-5H0z"/></svg>
  <svg class="arrow" style="left:418px;top:623px;" viewBox="0 0 18 18"><path d="M0 5h9V0l9 9-9 9v-5H0z"/></svg>
  <svg class="arrow" style="left:647px;top:631px;" viewBox="0 0 18 18"><path d="M0 5h9V0l9 9-9 9v-5H0z"/></svg>

  <div class="block legend meetings" style="left:901px;top:592px;width:163px;height:39px;">Meetings</div>
  <div class="block legend tools" style="left:901px;top:641px;width:163px;height:49px;">Emails/Tools</div>

</div>
</body>
</html>
```